Web Design Project - Event Management Company

A web-page design needs to be created for an event management company. The logo has already been created, the design needs to draw on the themes and colors of the logo and extend on that.

The event management company likes to differentiate itself from others by being a bit "un-conventional" and being able to think outside the box.

the specialise in corporate events, weddings, AGMs, anything that requires coordination of resources. They also can provide Audio Visual services such as recording events.

final design will also require HTML implementation

```html
<!DOCTYPE html>
<html lang="en">
<head>
<meta charset="utf-8">
<title>Odd Block Events</title>
<link href="https://fonts.googleapis.com/css2?family=Open+Sans:wght@300;400;600&display=swap" rel="stylesheet">
<style>
:root{
  --orange:#f0672a;
  --orange-light:#f58a5a;
  --pink:#e2185a;
  --bg:#232323;
  --panel:#111111;
  --panel-2:#1a1a1a;
  --line:#3a3a3a;
  --text:#e8e8e8;
  --muted:#8c8c8c;
  --white:#ffffff;
}
*{box-sizing:border-box;margin:0;padding:0}
html,body{width:1200px;height:3035px;overflow:hidden}
body{background:var(--bg);font-family:'Open Sans',Arial,sans-serif;color:var(--text);position:relative}
.abs{position:absolute}
.hero-backdrop{left:0;top:0;width:1200px;height:420px;background:linear-gradient(180deg,#4a4a4a 0%,#333 55%,var(--bg) 100%)}
.header{left:16px;top:61px;width:1168px;height:178px;background:rgba(20,20,20,.85)}
.logo{left:36px;top:77px;width:227px;height:142px;background:var(--white);border-radius:10px;display:flex;align-items:center;justify-content:center;gap:10px}
.logo-mark{width:22px;height:22px;background:var(--orange)}
.logo-name{font-size:18px;font-weight:600;color:#444;text-transform:uppercase;white-space:nowrap}
.social{top:117px;width:57px;height:61px;background:#3a3a3a;border:1px solid #4a4a4a;display:flex;align-items:center;justify-content:center}
.social span{width:14px;height:14px;background:#8a8a8a;border-radius:50%}
.stay{left:1024px;top:117px;width:136px;height:61px;background:#3a3a3a;border:1px solid #4a4a4a;font-size:11px;color:#aaa;display:flex;align-items:center;justify-content:center;text-transform:uppercase}
.nav{left:16px;top:261px;width:1168px;height:101px;background:var(--orange)}
.nav-item{top:22px;height:61px;line-height:61px;font-size:15px;color:var(--white);text-transform:uppercase;text-align:center;transform:translateX(-50%);white-space:nowrap}
.nav-item.active{left:88px;width:96px;background:var(--orange-light)}
.nav-sep{top:22px;width:1px;height:61px;background:#d4541c}
.search{left:966px;top:24px;width:129px;height:55px;background:var(--orange-light);font-size:13px;color:#fde;padding:17px 14px}
.search-btn{left:1095px;top:24px;width:49px;height:55px;background:#f7a07a}
.slider{left:40px;top:411px;width:1120px;height:496px;background:linear-gradient(160deg,#6a6a6a,#2a2a2a 70%,#1a1a1a)}
.slide-arrow{top:610px;width:40px;height:90px;background:rgba(0,0,0,.35)}
.caption{left:648px;top:785px;width:512px;height:65px;background:rgba(0,0,0,.6);font-size:30px;font-weight:300;color:var(--white);padding:10px 14px;white-space:nowrap}
.feature{top:931px;width:357px;height:198px;background:var(--orange);padding:24px 24px}
.feature h2{font-size:29px;font-weight:300;color:var(--white);text-transform:uppercase;display:flex;align-items:center;gap:12px;white-space:nowrap}
.feature p{font-size:16px;color:var(--white);margin-top:18px;line-height:1.55}
.feature .go{position:absolute;right:24px;bottom:18px;width:38px;height:38px;border-radius:50%;background:var(--orange-light)}
.heading{font-size:30px;font-weight:300;text-transform:uppercase;color:var(--text);border-bottom:3px solid var(--line);padding-bottom:6px;white-space:nowrap}
.heading::after{content:"";display:block;width:108px;height:4px;background:var(--orange);margin-top:4px;margin-bottom:-10px}
.mini-arrow{top:1196px;width:18px;height:18px;background:#3c3c3c}
.panel{background:var(--panel)}
.film-cover{left:58px;top:1269px;width:324px;height:324px;background:linear-gradient(135deg,#d8d8d8,#6a6a6a 60%,#2a2a2a)}
.shop-btn{top:1609px;height:36px;background:var(--orange);color:var(--white);font-size:13px;text-transform:uppercase;line-height:36px;text-align:center}
.player-bar{left:437px;top:1269px;width:324px;height:41px;background:#2a2a2a;font-size:12px;color:#bbb}
.playlist{left:437px;top:1330px;width:324px;height:313px;background:var(--panel-2);border:1px solid #333;padding:10px 20px}
.playlist li{list-style:none;font-size:14px;color:#999;height:46px;line-height:46px;border-bottom:1px solid #2c2c2c;white-space:nowrap}
.event{left:820px;width:320px}
.date{width:60px;height:113px;background:var(--orange);text-align:center;color:var(--white);font-size:13px;padding-top:10px;line-height:1.35}
.date b{display:block;font-size:22px;font-weight:600}
.event-title{left:79px;top:4px;font-size:16px;color:var(--text);white-space:nowrap}
.event-venue{left:79px;top:36px;font-size:14px;color:var(--muted);white-space:nowrap}
.event-tag{left:79px;top:66px;height:34px;padding:7px 14px;font-size:14px;white-space:nowrap}
.tag-buy{background:var(--orange);color:var(--white)}
.tag-off{background:#3c3c3c;color:#9a9a9a}
.post{left:40px;width:739px;height:184px;background:var(--panel)}
.post-thumb{left:18px;top:18px;width:244px;height:148px;background:linear-gradient(135deg,#8a8a8a,#2b2b2b)}
.post-title{left:280px;top:26px;font-size:24px;font-weight:400;color:var(--white);white-space:nowrap}
.post-meta{left:280px;top:70px;font-size:13px;color:var(--muted);white-space:nowrap}
.post-meta u{color:#aaa}
.post-meta .ic{color:var(--orange)}
.post-text{left:280px;top:100px;width:440px;font-size:14px;color:var(--muted);line-height:1.75}
.video{left:803px;top:1777px;width:357px;height:373px}
.video-img{left:18px;top:18px;width:321px;height:337px;background:linear-gradient(150deg,#7a7a7a,#262626)}
.reel{left:803px;top:2263px;width:357px;height:324px}
.reel-card{left:18px;top:18px;width:321px;height:290px;background:#f4f4f4;border-radius:6px}
.footer-line{left:16px;top:2641px;width:1168px;height:6px;background:var(--pink)}
.footer-flag{left:73px;top:2646px}
.footer-col{top:2716px;width:270px}
.footer-col h3{font-size:18px;font-weight:400;text-transform:uppercase;color:var(--text);margin-bottom:22px;white-space:nowrap}
.footer-col p{font-size:14px;color:var(--muted);line-height:1.6;margin-bottom:22px}
.footer-col li{list-style:none;font-size:14px;color:#aaa;border-bottom:1px solid var(--line);padding:7px 0;white-space:nowrap}
.thumb{width:71px;height:71px;background:linear-gradient(135deg,#9a9a9a,#3c3c3c)}
.copyright{left:0;top:2992px;width:1200px;height:43px;background:#1a1a1a;font-size:14px;color:#999;padding:12px 40px}
.copyright em{font-style:normal;color:var(--pink)}
</style>
</head>
<body>
<div class="abs hero-backdrop" role="img" aria-label="Black and white photo of a large conference hall audience"></div>

<header>
  <div class="abs header"></div>
  <div class="abs logo"><span class="logo-mark"></span><span class="logo-name">Odd Block Events</span></div>
  <a class="abs social" style="left:700px" aria-label="Social link"><span></span></a>
  <a class="abs social" style="left:765px" aria-label="Social link"><span></span></a>
  <a class="abs social" style="left:830px" aria-label="Social link"><span></span></a>
  <a class="abs social" style="left:895px" aria-label="Social link"><span></span></a>
  <a class="abs social" style="left:960px" aria-label="Feed"><span></span></a>
  <div class="abs stay">Stay Connected</div>
</header>

<nav class="abs nav">
  <div class="abs nav-item active">Home</div>
  <div class="abs nav-item" style="left:194px">Events</div>
  <div class="abs nav-sep" style="left:256px"></div>
  <div class="abs nav-item" style="left:318px">Audio</div>
  <div class="abs nav-sep" style="left:378px"></div>
  <div class="abs nav-item" style="left:437px">Video</div>
  <div class="abs nav-sep" style="left:500px"></div>
  <div class="abs nav-item" style="left:559px">Photo</div>
  <div class="abs nav-sep" style="left:620px"></div>
  <div class="abs nav-item" style="left:676px">Blog</div>
  <div class="abs nav-sep" style="left:735px"></div>
  <div class="abs nav-item" style="left:794px">Pages</div>
  <div class="abs search">Search...</div>
  <div class="abs search-btn"><svg width="49" height="55"><circle cx="23" cy="26" r="6" fill="none" stroke="#fff" stroke-width="2.5"/><line x1="27" y1="30" x2="31" y2="34" stroke="#fff" stroke-width="2.5"/></svg></div>
</nav>

<section>
  <div class="abs slider" role="img" aria-label="Audience applauding at a corporate gala, black and white"></div>
  <svg class="abs slide-arrow" style="left:40px"><polyline points="24,32 14,45 24,58" fill="none" stroke="#fff" stroke-width="2"/></svg>
  <svg class="abs slide-arrow" style="left:1120px"><polyline points="16,32 26,45 16,58" fill="none" stroke="#fff" stroke-width="2"/></svg>
  <div class="abs caption">Your Event Is Our Special Day</div>
</section>

<section>
  <div class="abs feature" style="left:40px"><h2><svg width="30" height="30"><rect x="2" y="13" width="7" height="15" fill="#fff"/><path d="M11 13 L17 3 Q21 3 20 9 L19 12 H27 Q29 13 28 16 L25 27 Q24 28 22 28 H11 Z" fill="#fff"/></svg>Corporate Days</h2><p>Conferences, AGMs and launches, planned to the minute.</p><span class="go"></span></div>
  <div class="abs feature" style="left:421px"><h2><svg width="30" height="30"><path d="M15 27 L3 14 Q0 5 8 4 Q13 4 15 9 Q17 4 22 4 Q30 5 27 14 Z" fill="#fff"/></svg>Weddings</h2><p>Venues, suppliers and timing, all handled for the day.</p><span class="go"></span></div>
  <div class="abs feature" style="left:803px"><h2><svg width="30" height="30"><path d="M4 20 V15 A11 11 0 0 1 26 15 V20" fill="none" stroke="#fff" stroke-width="3"/><rect x="2" y="17" width="7" height="11" fill="#fff"/><rect x="21" y="17" width="7" height="11" fill="#fff"/></svg>AV Recording</h2><p>Sound, screens and full video recording of your event.</p><span class="go"></span></div>
</section>

<section>
  <h2 class="abs heading" style="left:40px;top:1184px;width:357px">Event Films</h2>
  <svg class="abs mini-arrow" style="left:354px"><polyline points="11,5 7,9 11,13" fill="none" stroke="#999" stroke-width="1.5"/></svg>
  <svg class="abs mini-arrow" style="left:375px"><polyline points="7,5 11,9 7,13" fill="none" stroke="#999" stroke-width="1.5"/></svg>
  <h2 class="abs heading" style="left:421px;top:1184px;width:358px">Audio Player</h2>
  <h2 class="abs heading" style="left:803px;top:1184px;width:357px">Upcoming Events</h2>

  <div class="abs panel" style="left:40px;top:1249px;width:357px;height:394px"></div>
  <div class="abs film-cover" role="img" aria-label="Cover of a recorded conference film with speaker on stage"></div>
  <div class="abs shop-btn" style="left:58px;width:100px">Watch</div>
  <div class="abs shop-btn" style="left:170px;width:99px">Order</div>
  <div class="abs shop-btn" style="left:281px;width:77px">Share</div>

  <div class="abs panel" style="left:421px;top:1249px;width:358px;height:394px"></div>
  <div class="abs player-bar">
    <svg class="abs" style="left:10px;top:13px" width="14" height="16"><polygon points="2,1 13,8 2,15" fill="#fff"/></svg>
    <div class="abs" style="left:38px;top:16px;width:146px;height:9px;background:#111"></div>
    <div class="abs" style="left:220px;top:11px">00:00 / 03:26</div>
  </div>
  <ol class="abs playlist">
    <li>1.&nbsp; AGM Keynote 2013</li>
    <li>2.&nbsp; Gala Dinner Speech</li>
    <li>3.&nbsp; Wedding Vows Reel</li>
    <li>4.&nbsp; Product Launch</li>
    <li>5.&nbsp; Awards Night Intro</li>
    <li>6.&nbsp; Team Summit Panel</li>
  </ol>

  <div class="abs panel" style="left:803px;top:1249px;width:357px;height:415px"></div>
  <div class="abs event" style="top:1263px">
    <div class="date">23<b>Jan</b>2013</div>
    <div class="abs event-title">Annual General Meeting</div>
    <div class="abs event-venue">&#9679; Harbour Hall Centre</div>
    <div class="abs event-tag tag-buy">Book Seats</div>
  </div>
  <div class="abs" style="left:899px;top:1387px;width:243px;height:1px;background:var(--line)"></div>
  <div class="abs event" style="top:1400px">
    <div class="date">23<b>Jan</b>2013</div>
    <div class="abs event-title">Lane &amp; Brook Wedding</div>
    <div class="abs event-venue">&#9679; Harbour Hall Centre</div>
    <div class="abs event-tag tag-off">Sold Out</div>
  </div>
  <div class="abs" style="left:899px;top:1524px;width:243px;height:1px;background:var(--line)"></div>
  <div class="abs event" style="top:1537px">
    <div class="date">23<b>Jan</b>2013</div>
    <div class="abs event-title">Summer Staff Gala</div>
    <div class="abs event-venue">&#9679; Harbour Hall</div>
    <div class="abs event-tag tag-off">Canceled</div>
  </div>
</section>

<section>
  <h2 class="abs heading" style="left:40px;top:1713px;width:739px">Latest Blog</h2>
  <h2 class="abs heading" style="left:803px;top:1713px;width:357px">Latest Video</h2>

  <article class="abs post" style="top:1777px">
    <div class="abs post-thumb" role="img" aria-label="Speaker presenting at a company meeting"></div>
    <h3 class="abs post-title">Planning An AGM That Runs On Time</h3>
    <div class="abs post-meta"><span class="ic">&#9679;</span> <u>mkoller</u> &nbsp; <span class="ic">&#9679;</span> Feb 19, 2013 &nbsp; <span class="ic">&#9679;</span> <u>Image</u>, <u>Post</u> &nbsp; <span class="ic">&#9679;</span> <u>5</u></div>
    <p class="abs post-text">A clear run sheet, tested sound and one point of contact keep every item on schedule...</p>
  </article>
  <article class="abs post" style="top:1986px">
    <div class="abs post-thumb" role="img" aria-label="Banquet hall set for a gala dinner"></div>
    <h3 class="abs post-title">Welcome To Our Great Site</h3>
    <div class="abs post-meta"><span class="ic">&#9679;</span> <u>mkoller</u> &nbsp; <span class="ic">&#9679;</span> Feb 19, 2013 &nbsp; <span class="ic">&#9679;</span> <u>Night</u>, <u>Post</u> &nbsp; <span class="ic">&#9679;</span> <u>0</u></div>
    <p class="abs post-text">We bring venues, suppliers, people and equipment together so your day simply works...</p>
  </article>
  <article class="abs post" style="top:2196px">
    <div class="abs post-thumb" role="img" aria-label="Camera operator filming a wedding ceremony"></div>
    <h3 class="abs post-title">Full HD Recording For Your Event</h3>
    <div class="abs post-meta"><span class="ic">&#9679;</span> <u>mkoller</u> &nbsp; <span class="ic">&#9679;</span> Feb 19, 2013 &nbsp; <span class="ic">&#9679;</span> <u>Image</u>, <u>Post</u> &nbsp; <span class="ic">&#9679;</span> <u>0</u></div>
    <p class="abs post-text">Multi-camera filming, clean audio and an edited film delivered within two weeks...</p>
  </article>
  <article class="abs post" style="top:2405px">
    <div class="abs post-thumb" role="img" aria-label="Guests dancing at a wedding reception"></div>
    <h3 class="abs post-title">Harbour Hall White Wedding Show</h3>
    <div class="abs post-meta"><span class="ic">&#9679;</span> <u>mkoller</u> &nbsp; <span class="ic">&#9679;</span> Feb 19, 2013 &nbsp; <span class="ic">&#9679;</span> <u>Night</u>, <u>Post</u> &nbsp; <span class="ic">&#9679;</span> <u>0</u></div>
    <p class="abs post-text">Meet our planners, see table layouts and book a free consultation for your big day...</p>
  </article>

  <div class="abs video panel"><div class="abs video-img" role="img" aria-label="Video still of guests celebrating at an evening reception"></div></div>

  <h2 class="abs heading" style="left:803px;top:2198px;width:357px">Showreel</h2>
  <div class="abs reel panel">
    <div class="abs reel-card">
      <div class="abs" style="left:14px;top:16px;width:46px;height:46px;border-radius:50%;background:var(--pink)"></div>
      <svg class="abs" style="left:30px;top:29px" width="18" height="20"><polygon points="2,1 16,10 2,19" fill="#fff"/></svg>
      <div class="abs" style="left:70px;top:14px;font-size:12px;color:#666">oddblockevents/av...</div>
      <div class="abs" style="left:70px;top:34px;font-size:16px;font-weight:600;color:#333">AV Showreel ...</div>
      <div class="abs" style="left:6px;top:80px;width:309px;height:86px;background:linear-gradient(180deg,#bbb,#7a7a7a)" role="img" aria-label="Audio waveform"></div>
      <div class="abs" style="left:14px;top:210px;font-size:11px;color:#999">&#9654; 1,989,923 &nbsp; &#9829; 38,533 &nbsp; &#8635; 6,365 &nbsp; &#9679; 3,030</div>
    </div>
  </div>
</section>

<footer>
  <div class="abs footer-line"></div>
  <svg class="abs footer-flag" width="40" height="34"><polygon points="0,0 40,0 0,34" fill="#e2185a"/></svg>
  <div class="abs footer-col" style="left:40px">
    <h3>About Us</h3>
    <p>We plan corporate events, weddings and AGMs, and coordinate every resource they need.</p>
    <p>Our in-house AV team supplies sound, lighting and screens, and records your event in full so nothing is lost.</p>
  </div>
  <div class="abs footer-col" style="left:326px;width:262px">
    <h3>Latest Posts</h3>
    <ul>
      <li>Planning An AGM That Runs On Time</li>
      <li>Welcome To Our Great Site</li>
      <li>Full HD Recording For Your Event</li>
      <li>Harbour Hall White Wedding Show</li>
      <li>This Is An Awesome Image Post</li>
    </ul>
  </div>
  <div class="abs footer-col" style="left:613px">
    <h3>Event Photos</h3>
  </div>
  <div class="abs thumb" style="left:613px;top:2755px" role="img" aria-label="Event photo thumbnail"></div>
  <div class="abs thumb" style="left:698px;top:2755px" role="img" aria-label="Event photo thumbnail"></div>
  <div class="abs thumb" style="left:785px;top:2755px" role="img" aria-label="Event photo thumbnail"></div>
  <div class="abs thumb" style="left:613px;top:2848px" role="img" aria-label="Event photo thumbnail"></div>
  <div class="abs thumb" style="left:698px;top:2848px" role="img" aria-label="Event photo thumbnail"></div>
  <div class="abs thumb" style="left:785px;top:2848px" role="img" aria-label="Event photo thumbnail"></div>
  <div class="abs footer-col" style="left:899px">
    <h3>Latest Tweets</h3>
    <p style="font-weight:600;color:#bbb">Follow Us on Chirper! &raquo;</p>
  </div>
  <div class="abs copyright">&copy; Copyright 2013 <em>Odd Block Events</em>. All Rights Reserved.</div>
</footer>
</body>
</html>
```